Business Card Design

i need a business card to promote my Handyman & Gardening business. It would be nice to see a design incorporating both of these things. We are happy to help in any way we can with no job ever being to small.

Industry/Entity Type

Business

Contact Information for Business Card

Dave's Handyman & Gardening Service
Dave Holt
PO Box 312 Marrowvale SA 5470
dave.holt@fernmail.com
ph 0412 736 508

```html
<!DOCTYPE html>
<html lang="en">
<head>
<meta charset="utf-8">
<title>Dave's Handyman &amp; Gardening Service – Business Card</title>
<link rel="stylesheet" href="https://fonts.googleapis.com/css2?family=Open+Sans:wght@400;700&display=swap">
<style>
  :root {
    --page: #ffffff;
    --card-dark: #2e2e2f;
    --card-band: #373738;
    --stripe-light: #e6e6e6;
    --stripe-grey: #b9b9b9;
    --leaf-green: #8cc414;
    --text-light: #f2f2f2;
    --text-soft: #d9d9d9;
  }
  html, body {
    margin: 0;
    width: 1200px;
    height: 1025px;
    overflow: hidden;
    background: var(--page);
  }
  .business-card {
    position: absolute;
    left: 100px;
    top: 226px;
    width: 1000px;
    height: 572px;
    background: var(--card-dark);
    overflow: hidden;
    font-family: "Open Sans", Arial, sans-serif;
    color: var(--text-light);
    box-shadow: 0 2px 14px rgba(0,0,0,0.18);
  }
  .contact-band {
    position: absolute;
    left: 0; right: 0;
    top: 256px;
    height: 176px;
    background: var(--card-band);
  }
  .divider-stripe {
    position: absolute;
    left: 0; right: 0;
    top: 432px;
    height: 14px;
    background: linear-gradient(var(--stripe-light) 0 55%, var(--stripe-grey) 55% 100%);
  }
  .green-band {
    position: absolute;
    left: 0; right: 0;
    top: 446px;
    height: 96px;
    background: var(--leaf-green);
  }
  .card-edge {
    position: absolute;
    left: 0; right: 0;
    top: 542px;
    bottom: 0;
    background: var(--stripe-light);
  }
  .brand {
    position: absolute;
    left: 58px;
    top: 168px;
    display: flex;
    align-items: flex-start;
    gap: 18px;
  }
  .brand-square {
    width: 72px;
    height: 72px;
    border-radius: 8px;
    background: var(--leaf-green);
  }
  .brand-name {
    margin: 44px 0 0;
    font-weight: 700;
    font-size: 21px;
    line-height: 1.3;
    letter-spacing: 0.04em;
    text-transform: uppercase;
    text-align: center;
    color: var(--text-light);
  }
  .brand-short {
    position: absolute;
    right: 80px;
    top: 150px;
    margin: 0;
    font-weight: 700;
    font-size: 64px;
    letter-spacing: 0.04em;
    text-transform: uppercase;
    color: var(--text-light);
  }
  .contact {
    position: absolute;
    display: flex;
    align-items: flex-start;
    gap: 10px;
    font-size: 19px;
    line-height: 1.6;
    color: var(--text-soft);
  }
  .contact svg { flex: none; margin-top: 5px; }
  .contact-address { left: 58px; top: 276px; }
  .contact-phone { left: 392px; top: 352px; }
  .contact-email { right: 60px; top: 388px; }
</style>
</head>
<body>
  <div class="business-card">
    <div class="contact-band"></div>
    <div class="divider-stripe"></div>
    <div class="green-band"></div>
    <div class="card-edge"></div>

    <div class="brand">
      <div class="brand-square"></div>
      <h1 class="brand-name">Handyman &amp; Gardening<br>Service</h1>
    </div>
    <p class="brand-short">Dave's</p>

    <div class="contact contact-address">
      <svg width="14" height="20" viewBox="0 0 14 20" aria-hidden="true">
        <path d="M7 0C3.1 0 0 3.1 0 7c0 5 7 13 7 13s7-8 7-13c0-3.9-3.1-7-7-7zm0 10a3 3 0 1 1 0-6 3 3 0 0 1 0 6z" fill="#8cc414"/>
      </svg>
      <span>Dave Holt PO Box 312<br>Marrowvale SA 5470</span>
    </div>

    <div class="contact contact-phone">
      <svg width="14" height="20" viewBox="0 0 14 20" aria-hidden="true">
        <path d="M3 1l3 0 1 5-2 1.5c.8 2.4 2 4.2 3.6 5.5L10.5 11 14 13.5 12.5 17C6 16.5 1.5 9 3 1z" fill="#8cc414"/>
      </svg>
      <span>0412 736 508</span>
    </div>

    <div class="contact contact-email">
      <span>dave.holt@fernmail.com</span>
    </div>
  </div>
</body>
</html>
```